Tales from Kin Logo Design plus business cards design

We are a start up company that will help seniors write their memoirs...beginning with a few ancestors and their heritage and continuing through their own history...how they would like to be remembered in the next generation. I envision a card with a senior citizen at an older writing desk, writing her memoirs, with a book (maybe standing on top, leaning slightly) that has the words Tales from Kin.com on the back binding. OR maybe a senior couple walking into the sunset with the same book somewhere in the frame. Communicating the relevance of every life being significant to those that come after them...when a genealogy doesn't say enough about the details of ones life. Please note that I am open to the professionals own ideas...I am not locked into my concepts. On the back of the card I would like one or two phrases..."A Genealogy Doesn't Say Enough" and/or "Every life legacy is uniquely significant to the next generation".
Updates

I have added a couple of photos for ideas that may be used if needed.

I have both increased and committed the payment! Thanks for the reminder!

Reason: We increased the payment commitment and added some photo ideas to help.

We want to thank EVERYONE who participated in this contest. There were so many wonderful and VERY professional proposals...making it very challenging to decide on one! We are posting a new contest for a brochure now and hope many of you will participate. May God bless your endeavors.

Target Market(s)

Senior populous & baby boomer generation.

Industry/Entity Type

Business

Logo Text

Tales from Kin ordinary lives...extraordinary legacy

Requirements
Must have
• Relevant info:
Domain name: talesfromkin.com
email: info@talesfromkin.com
phone: 1-855-GAB-TALE toll free
1-717-382-5619 local
name: Doris Whitlock, M.A.
Nice to have
• photo of senior or senior couple....book with our web address on the binding. I attached two photos that could work if cropped and enhanced. Words need to be deleted from the one photo of senior at a writing desk and couple on the beach could use a sunset sky and other people cropped out. Just ideas...don't know if you have better ones or prefer a different idea.

```html
<!DOCTYPE html>
<html lang="en">
<head>
<meta charset="utf-8">
<title>Tales from Kin – Business Card</title>
<link href="https://fonts.googleapis.com/css2?family=Cinzel:wght@400;700&display=swap" rel="stylesheet">
<style>
  :root {
    --stage: #4d4d4d;
    --orchid: #c05ab0;
    --orchid-light: #e08cd0;
    --orchid-deep: #9a3f8e;
    --ink: #0d0a0a;
    --text-light: #f3ece8;
    --warm-photo: #8a5e52;
    --warm-dark: #3a2622;
    --sunset: #d9683a;
    --dusk: #6c4a48;
  }
  html, body {
    margin: 0;
    width: 1200px;
    height: 750px;
    overflow: hidden;
    background: var(--stage);
    font-family: "Cinzel", serif;
  }
  .card {
    position: absolute;
    top: 209px;
    width: 525px;
    height: 300px;
    border-radius: 14px;
    overflow: hidden;
    background: var(--ink);
  }
  .card-front { left: 68px; }
  .card-back { left: 613px; }

  .photo {
    position: absolute;
    inset: 0;
  }
  .card-front .photo {
    background:
      linear-gradient(180deg, var(--sunset) 0%, #b85a44 30%, var(--dusk) 55%, #2d2322 100%) right / 290px 100% no-repeat,
      linear-gradient(90deg, var(--warm-photo) 0%, #6a443c 45%, var(--warm-dark) 100%) left / 240px 100% no-repeat;
  }
  .card-front .photo::after {
    content: "";
    position: absolute;
    inset: 0;
    background: linear-gradient(90deg, transparent 35%, rgba(20,12,12,.55) 46%, transparent 58%);
  }
  .card-back .photo {
    background: linear-gradient(90deg,
      var(--warm-photo) 0%, #5e3e38 22%, #2a1c1b 36%, var(--ink) 42%,
      var(--ink) 60%, #2a1c1b 65%, #5e3e38 78%, var(--warm-photo) 100%);
  }

  .brand-name {
    position: absolute;
    margin: 0;
    color: var(--orchid);
    font-weight: 700;
    letter-spacing: 1px;
    white-space: nowrap;
  }
  .card-front .brand-name { left: 28px; top: 42px; font-size: 30px; }
  .card-back .brand-name { left: 0; right: 0; top: 128px; text-align: center; font-size: 32px; }

  .name-tab {
    position: absolute;
    left: 0;
    top: 116px;
    width: 12px;
    height: 56px;
    background: var(--orchid);
    border-radius: 0 6px 6px 0;
  }
  .holder-name {
    position: absolute;
    left: 28px;
    top: 135px;
    margin: 0;
    color: var(--orchid);
    font-size: 14px;
    font-weight: 700;
  }
  .contact-list {
    position: absolute;
    left: 28px;
    top: 190px;
    margin: 0;
    padding: 0;
    list-style: none;
    color: var(--text-light);
    font-size: 11px;
    line-height: 15px;
  }
  .contact-list li { display: flex; align-items: center; gap: 8px; }
  .contact-list svg { width: 12px; height: 12px; fill: var(--orchid); flex: none; }

  .wave { position: absolute; left: 0; top: 0; width: 525px; height: 300px; }
</style>
</head>
<body>

<section class="card card-front">
  <div class="photo" role="img" aria-label="Photo of a senior woman writing at an old desk, blending into a senior couple walking along a beach at sunset"></div>
  <p class="brand-name">Tales from Kin</p>
  <span class="name-tab"></span>
  <p class="holder-name">Doris Whitlock, M.A.</p>
  <ul class="contact-list">
    <li><svg viewBox="0 0 24 24"><path d="M6.6 10.8a15 15 0 0 0 6.6 6.6l2.2-2.2c.3-.3.7-.4 1-.2 1.1.4 2.3.6 3.6.6.6 0 1 .4 1 1V20c0 .6-.4 1-1 1A17 17 0 0 1 3 4c0-.6.4-1 1-1h3.5c.6 0 1 .4 1 1 0 1.3.2 2.5.6 3.6.1.3 0 .7-.2 1z"/></svg>1-855-GAB-TALE toll free</li>
    <li><svg viewBox="0 0 24 24"><path d="M6.6 10.8a15 15 0 0 0 6.6 6.6l2.2-2.2c.3-.3.7-.4 1-.2 1.1.4 2.3.6 3.6.6.6 0 1 .4 1 1V20c0 .6-.4 1-1 1A17 17 0 0 1 3 4c0-.6.4-1 1-1h3.5c.6 0 1 .4 1 1 0 1.3.2 2.5.6 3.6.1.3 0 .7-.2 1z"/></svg>1-717-382-5619 local</li>
    <li><svg viewBox="0 0 24 24"><path d="M2 5h20v14H2z M2 5l10 8 10-8" /></svg>info@talesfromkin.com</li>
    <li><svg viewBox="0 0 24 24"><circle cx="12" cy="12" r="10"/></svg>www.talesfromkin.com</li>
  </ul>
  <svg class="wave" viewBox="0 0 525 300" aria-hidden="true">
    <defs>
      <linearGradient id="orchidBand" x1="0" x2="1">
        <stop offset="0" stop-color="var(--orchid-deep)"/>
        <stop offset=".5" stop-color="var(--orchid-light)"/>
        <stop offset="1" stop-color="var(--orchid)"/>
      </linearGradient>
    </defs>
    <path d="M0 258 C70 272 150 282 230 272 C300 262 330 246 380 244 L525 246 L525 300 L0 300Z" fill="#111"/>
    <path d="M0 262 C70 278 150 286 230 276" stroke="#bbb" stroke-width="1.5" fill="none"/>
    <path d="M0 272 C120 292 220 250 330 244 C420 240 480 250 525 252 L525 300 L0 300Z" fill="url(#orchidBand)"/>
  </svg>
</section>

<section class="card card-back">
  <div class="photo" role="img" aria-label="Mirrored photos of a senior woman writing at a desk on both sides, fading to black in the centre"></div>
  <p class="brand-name">Tales from Kin</p>
</section>

</body>
</html>
```